Lawn mowing business card design

We need a business card design for our lawn mowing and gardening business which is located in the Northern Beaches of Sydney. Our business name is Meadowline Turf and our logo is predominantly green and yellow in color. Please see our website at www.meadowlineturf.com.au for design ideas. The business targets young professionals and older clientele. As such the font should be easy to read, but I also want the business card to be colorful and stand out.

Target Market(s)

young professionals

Industry/Entity Type

Lawn Care

Contact Information for Business Card

Meadowline Turf, Gareth Pellow, 0478559201, www.meadowlineturf.com.au, email: meadowlineturf@mailbox-example.com

Font styles to use
Serif

Colors
9bcb3b
fbed22

Requirements
Must have
• Must include the details listed above. Must include the attached logo.
Nice to have
• Logo attached with two copies. The logo without any writing is high quality, please feel free to be creative with the text stating our business name "Meadowline Turf" using this file.

```html
<!DOCTYPE html>
<html lang="en">
<head>
<meta charset="utf-8">
<title>Meadowline Turf – Business Card</title>
<link href="https://fonts.googleapis.com/css2?family=Open+Sans:wght@400;600;700&display=swap" rel="stylesheet">
<style>
  :root {
    --stage: #ecebe8;
    --card: #ffffff;
    --green-light: #8cc63f;
    --green-dark: #16853a;
    --brand-green: #1f7a34;
    --brand-yellow: #fbed22;
    --text-light: #ffffff;
    --rule: rgba(255,255,255,0.28);
  }
  * { margin: 0; padding: 0; box-sizing: border-box; }
  html, body {
    width: 1200px; height: 900px; overflow: hidden;
    background: var(--stage);
    font-family: "Open Sans", Arial, sans-serif;
  }
  .canvas { position: relative; width: 1200px; height: 900px; }
  .card {
    position: absolute;
    background: var(--card);
    box-shadow: 0 6px 20px rgba(0,0,0,0.15);
    overflow: hidden;
  }
  .card-front { left: 77px; top: 33px; width: 589px; height: 365px; }
  .card-back { left: 388px; top: 505px; width: 567px; height: 352px; }

  .brand {
    position: absolute;
    display: flex; align-items: center; gap: 10px;
    color: var(--brand-green);
    font-weight: 700;
    white-space: nowrap;
  }
  .brand-mark { display: block; background: var(--brand-yellow); border: 0; }
  .card-front .brand { left: 50px; top: 72px; font-size: 22px; }
  .card-front .brand-mark { width: 22px; height: 22px; }
  .card-back .brand {
    left: 50%; top: 50%; transform: translate(-50%, -50%);
    font-size: 32px; gap: 14px;
  }
  .card-back .brand-mark { width: 30px; height: 30px; }

  .contact-band {
    position: absolute; left: 0; right: 0; top: 183px; bottom: 0;
    background: linear-gradient(180deg, var(--green-light) 0%, var(--green-dark) 100%);
    color: var(--text-light);
    padding: 20px 0 0 32px;
  }
  .holder-name { font-size: 21px; font-weight: 600; line-height: 30px; margin-bottom: 6px; }
  .contact-list { list-style: none; width: 248px; }
  .contact-item {
    display: flex; align-items: center;
    height: 36px;
    border-top: 1px solid var(--rule);
    font-size: 14.5px; white-space: nowrap;
  }
  .contact-icon { width: 13px; height: 13px; margin: 0 14px 0 1px; flex: none; }
</style>
</head>
<body>
<main class="canvas">
  <section class="card card-front">
    <div class="brand">
      <span class="brand-mark"></span>
      <span class="brand-name">Meadowline Turf</span>
    </div>
    <div class="contact-band">
      <p class="holder-name">Gareth Pellow</p>
      <ul class="contact-list">
        <li class="contact-item">
          <svg class="contact-icon" viewBox="0 0 16 16" aria-hidden="true"><path fill="#fff" d="M3.5 1l2.5 3-1.5 1.8c.8 1.9 2.2 3.3 4.1 4.2L10.4 8.5l3.1 2.4-1.3 3C6.5 13.6 2.4 9.5 1.9 3.4z"/></svg>
          <span>0478559201</span>
        </li>
        <li class="contact-item">
          <svg class="contact-icon" viewBox="0 0 16 16" aria-hidden="true"><rect x="1" y="3" width="14" height="10" fill="#fff"/><path d="M1.5 3.5L8 8.5l6.5-5" fill="none" stroke="#3a9a3c" stroke-width="1.3"/></svg>
          <span>meadowlineturf@mailbox-example.com</span>
        </li>
        <li class="contact-item">
          <svg class="contact-icon" viewBox="0 0 16 16" aria-hidden="true"><g fill="none" stroke="#fff" stroke-width="1.8" stroke-linecap="round"><path d="M6.5 9.5l3-3"/><path d="M7.5 4.5l1.5-1.5a2.5 2.5 0 013.5 3.5L11 8"/><path d="M8.5 11.5L7 13a2.5 2.5 0 01-3.5-3.5L5 8"/></g></svg>
          <span>www.meadowlineturf.com.au</span>
        </li>
      </ul>
    </div>
  </section>

  <section class="card card-back">
    <div class="brand">
      <span class="brand-mark"></span>
      <span class="brand-name">Meadowline Turf</span>
    </div>
  </section>
</main>
</body>
</html>
```